Summer Special Membership Drive

Looking to run a "Summer Special" on 12 month Memberships for Jan/Feb 2020 to boost membership number up. This is a great time to get people exercising and everyone loves a New Year Sale. Special is designed to attract more people to join and enjoy the savings.
Artwork will be display via social media (SN and Snapvista) as well as in store. Artwork must be eye catching and direct to the customer. Customer should feel a sense of relief with being able to exercise at a lower cost .

Artwork to be formatted in A0 for poster and Chatterly cover and snapvista

Heading: "Summer Sale or Summer Special"
12 Months
$350.00 Save over 20%
Terms and conditions apply"
*Offer End 28th February

New Opening Time
Weekdays from 5:00am starting 13th January

below are other promos we had designed on Pixel Bazaar along with potential photos to be included into this promo

Target Market(s)

16-50 male and female

Industry/Entity Type

Fitness

Colors

Designer to choose colors to be used in the design.

Requirements
Must have
• Lots of color and a summer theme. Attached is a 12 month special from last year.
• Contact details
• Address: 14 Larch Rd Bellmore Park
• Ph: 8147 2650
• Web: www.ironleaffitness.com.au
Nice to have
• Male and female in the artwork, They don't need to be the center of attention either

```html
<!DOCTYPE html>
<html lang="en">
<head>
<meta charset="utf-8">
<title>Ironleaf Fitness – Summer Sale</title>
<link rel="stylesheet" href="https://fonts.googleapis.com/css2?family=Montserrat:wght@400;500;600;800;900&family=Open+Sans:wght@400&display=swap">
<style>
  :root {
    --red: #ed1c24;
    --white: #ffffff;
    --brick-dark: #1e1510;
    --brick-mid: #4a3526;
    --skin-light: #a5704c;
    --skin-dark: #5e3b27;
    --pants: #2b2b2d;
    --fine-print: #8c8c8c;
  }
  * { margin: 0; padding: 0; box-sizing: border-box; }
  html, body { width: 1200px; height: 951px; overflow: hidden; background: var(--brick-dark); }
  .poster { position: relative; width: 1200px; height: 951px; overflow: hidden; font-family: "Montserrat", sans-serif; }
  .wall-photo {
    position: absolute; inset: 0;
    background: radial-gradient(ellipse at 45% 40%, var(--brick-mid) 0%, var(--brick-dark) 75%);
  }
  .layer { position: absolute; inset: 0; width: 1200px; height: 951px; }
  .athlete-photo {
    position: absolute; left: 100px; top: 8px; width: 630px; height: 905px;
    border-radius: 240px 240px 24px 24px;
    background: linear-gradient(180deg, var(--skin-light) 0%, var(--skin-dark) 62%, var(--pants) 70%, var(--pants) 100%);
  }
  .headline { font-family: "Montserrat", sans-serif; font-weight: 900; }
  .offer-line { font-family: "Montserrat", sans-serif; font-weight: 600; }
  .timings { font-family: "Montserrat", sans-serif; font-weight: 400; fill: var(--white); }
  .brand-name { font-family: "Montserrat", sans-serif; font-weight: 800; fill: var(--white); }
  .fine-print { font-family: "Open Sans", sans-serif; fill: var(--fine-print); }
  .contact-bar { font-family: "Montserrat", sans-serif; font-weight: 400; fill: var(--white); }
</style>
</head>
<body>
<main class="poster">
  <div class="wall-photo" role="img" aria-label="Photo of a dark brick gym wall"></div>

  <svg class="layer bands" viewBox="0 0 2156 1708" preserveAspectRatio="none" aria-hidden="true">
    <polygon points="0,318 2156,222 2156,238 0,335" fill="var(--red)"/>
    <polygon points="0,335 2156,238 2156,718 0,810" fill="var(--white)"/>
    <polygon points="0,810 2156,718 2156,735 0,828" fill="var(--red)"/>
    <polygon points="0,872 2156,785 2156,935 0,1000" fill="var(--red)"/>
    <polygon points="0,1030 2156,940 2156,1090 0,1155" fill="var(--white)"/>
    <polygon points="0,1188 2156,1110 2156,1250 0,1320" fill="var(--red)"/>
  </svg>

  <div class="athlete-photo" role="img" aria-label="Photo of a muscular man holding two dumbbells"></div>

  <svg class="layer copy" viewBox="0 0 2156 1708" preserveAspectRatio="none">
    <g class="brand">
      <text class="brand-name" x="1210" y="140" font-size="118" textLength="500" lengthAdjust="spacingAndGlyphs">IRONLEAF</text>
      <text class="brand-name" x="1210" y="205" font-size="52" textLength="500" lengthAdjust="spacing" letter-spacing="10">FITNESS</text>
    </g>

    <g class="headline" transform="rotate(-2.6 1530 500)">
      <g font-size="250">
        <text x="1035" y="495" textLength="985" lengthAdjust="spacingAndGlyphs" fill="none" stroke="var(--red)" stroke-width="22" stroke-linejoin="round">SUMMER</text>
        <text x="1035" y="495" textLength="985" lengthAdjust="spacingAndGlyphs" fill="none" stroke="var(--white)" stroke-width="12" stroke-linejoin="round">SUMMER</text>
        <text x="1035" y="495" textLength="985" lengthAdjust="spacingAndGlyphs" fill="var(--red)">SUMMER</text>
        <text x="1235" y="668" textLength="590" lengthAdjust="spacingAndGlyphs" fill="none" stroke="var(--red)" stroke-width="22" stroke-linejoin="round">SALE</text>
        <text x="1235" y="668" textLength="590" lengthAdjust="spacingAndGlyphs" fill="none" stroke="var(--white)" stroke-width="12" stroke-linejoin="round">SALE</text>
        <text x="1235" y="668" textLength="590" lengthAdjust="spacingAndGlyphs" fill="var(--red)">SALE</text>
      </g>
    </g>

    <g class="offer-line" transform="rotate(-2.6 1290 905)">
      <text x="1290" y="905" font-size="78" fill="var(--white)">12 Months</text>
      <circle cx="1738" cy="862" r="13" fill="var(--white)"/>
      <text x="1830" y="900" font-size="78" fill="var(--white)">350$</text>
    </g>
    <text class="offer-line" x="1325" y="1062" font-size="68" fill="var(--red)" transform="rotate(-2.6 1325 1062)">Offer valid till 28<tspan dy="-30" font-size="38">th</tspan><tspan dy="30"> Feb.</tspan></text>
    <text class="offer-line" x="1335" y="1228" font-size="84" fill="var(--white)" transform="rotate(-2.6 1335 1228)">Flat 20% off</text>

    <g class="timings" font-size="48">
      <text x="1425" y="1422">New Batch Timings:</text>
      <text x="1442" y="1490">Weekdays, 5:00am</text>
      <text x="1425" y="1558">Starting from 13th Jan.</text>
    </g>

    <text class="fine-print" x="2" y="1634" font-size="24">*Terms and conditions applied</text>

    <rect x="0" y="1645" width="2156" height="63" fill="var(--red)"/>
    <text class="contact-bar" x="1078" y="1691" font-size="42" text-anchor="middle" textLength="1920" lengthAdjust="spacingAndGlyphs" xml:space="preserve">Address: 14 Larch Rd Bellmore Park    Ph.: 8147 2650    Website: www.ironleaffitness.com.au</text>
  </svg>
</main>
</body>
</html>
```